serious, thorough, light and simple - that's my advice and mediations

My business card should combine my logo (uploaded file) and my homepage (https://fellor-mediation.webnestsite.com).

Contact Information for Business Card

Name: Sabine Fellor di Vanti
Phone: 076 412 58 94
mail: sfellor@postkiv.ch
web: www.fellor-di-vanti.ch

```html
<!DOCTYPE html>
<html lang="de">
<head>
<meta charset="utf-8">
<title>Raum für Klärung – Visitenkarte</title>
<link rel="stylesheet" href="https://fonts.googleapis.com/css2?family=Open+Sans:wght@400;600&family=Roboto:wght@400&family=Playball&display=swap">
<style>
  :root {
    --backdrop: #c9c9c9;
    --navy: #1f3a6e;
    --teal: #14505a;
    --forest: #0b6334;
    --paper: #f4f4f3;
    --ink: #3c3c3c;
    --name-green: #14693a;
    --white: #ffffff;
  }
  * { margin: 0; padding: 0; box-sizing: border-box; }
  html, body {
    width: 1200px; height: 576px; overflow: hidden;
    background: var(--backdrop);
  }
  .canvas { position: relative; width: 1200px; height: 576px; }

  .card {
    position: absolute;
    width: 484px; height: 291px;
    box-shadow: 0 3px 6px rgba(0,0,0,0.25);
    overflow: hidden;
  }

  /* Front */
  .card--front {
    left: 82px; top: 139px;
    background: linear-gradient(30deg, var(--navy) 0%, var(--teal) 50%, var(--forest) 100%);
  }
  .card--front .brand {
    position: absolute; left: 0; right: 0; top: 108px;
    display: flex; align-items: center; justify-content: center; gap: 12px;
  }
  .brand__dot {
    width: 14px; height: 14px; border-radius: 50%;
    border: 2px solid var(--white);
  }
  .card--front .brand__name {
    font-family: "Open Sans", sans-serif; font-weight: 400;
    font-size: 32px; color: var(--white); letter-spacing: 0.5px;
  }
  .card--front .homepage {
    position: absolute; left: 0; right: 0; top: 250px;
    text-align: center;
    font-family: "Open Sans", sans-serif; font-size: 12.5px;
    color: #e4ecea; letter-spacing: 0.2px;
  }

  /* Back */
  .card--back {
    left: 602px; top: 138px;
    background: var(--paper);
  }
  .card--back .brand {
    position: absolute; left: 36px; top: 126px;
    display: flex; align-items: center; gap: 8px;
  }
  .card--back .brand__dot { border-color: var(--navy); width: 12px; height: 12px; }
  .card--back .brand__name {
    font-family: "Open Sans", sans-serif; font-weight: 400;
    font-size: 22px; color: var(--forest);
  }
  .contact { position: absolute; left: 264px; top: 102px; }
  .contact__name {
    font-family: "Playball", cursive; font-size: 21px;
    color: var(--name-green); margin-bottom: 8px;
  }
  .contact__list { list-style: none; }
  .contact__item {
    display: flex; align-items: center; gap: 10px;
    font-family: "Roboto", sans-serif; font-size: 13.5px;
    color: var(--ink); height: 18px; margin-left: 6px;
  }
  .contact__icon { width: 11px; height: 11px; fill: var(--navy); flex: none; }
  .card__band {
    position: absolute; left: 0; right: 0; bottom: 0; height: 11px;
    background: linear-gradient(90deg, var(--navy), var(--teal) 50%, var(--forest));
  }
</style>
</head>
<body>
<main class="canvas">
  <section class="card card--front" aria-label="Vorderseite">
    <div class="brand">
      <span class="brand__dot"></span>
      <span class="brand__name">Raum für Klärung</span>
    </div>
    <p class="homepage">www.fellor-mediation.webnestsite.com</p>
  </section>

  <section class="card card--back" aria-label="Rückseite">
    <div class="brand">
      <span class="brand__dot"></span>
      <span class="brand__name">Raum für Klärung</span>
    </div>
    <div class="contact">
      <p class="contact__name">Sabine Fellor di Vanti</p>
      <ul class="contact__list">
        <li class="contact__item">
          <svg class="contact__icon" viewBox="0 0 12 12" aria-hidden="true"><path d="M1 3c0-1 1-2 5-2s5 1 5 2v1H8V3H4v1H1zM3 5h6l2 3v3H1V8z"/></svg>
          076 412 58 94
        </li>
        <li class="contact__item">
          <svg class="contact__icon" viewBox="0 0 12 12" aria-hidden="true"><path d="M0 2h12v8H0zM1 3v.4l5 3.2 5-3.2V3z" fill-rule="evenodd"/></svg>
          sfellor@postkiv.ch
        </li>
        <li class="contact__item">
          <svg class="contact__icon" viewBox="0 0 12 12" aria-hidden="true"><circle cx="6" cy="6" r="5.5"/><path d="M0.5 6h11M6 0.5c-3 3-3 8 0 11M6 0.5c3 3 3 8 0 11" stroke="#f4f4f3" stroke-width="0.8" fill="none"/></svg>
          www.fellor-di-vanti.ch
        </li>
      </ul>
    </div>
    <div class="card__band"></div>
  </section>
</main>
</body>
</html>
```